Maple Lantern Kids - pictora Photospot

We are looking for an pictora type wal for our pediatric dental office. We are thinking it could be weaved into a whole bunch of what we do (i.e. potentially water marked or faded in the background on letterhead, as an pictroa type wall in the practice, as a banner or section of the home page on the website, on rack cards, etc.) I’m thinking it would utilize a nice fun cursive script for the wording "Maple Lantern Kids is the spot for...." and a bunch of different sized “spots” with meaningful words that speak to who we are. That list would include things like:

• Fun
• Smiles
• Laughter
• Caring
• Comfort
• Amazing
• Kids
• Toddlers
• Teens
• Friends
• Family
• Health
• Education
• Cheer
• Positivity
• Exceptional Care

From a color perspective….we could look at a couple of options. We could have one version that has it washed out and in the background (more subliminal). We could have one version that was consistent with the colors in our logo. And we could have one version that popped with more color by utilizing the colors in some of the artwork we use throughout the office (snowboard picture as an example)

Target Market(s)

Appeal to hip families with kids

Industry/Entity Type

Pediatric Dental

Font styles to use
Other font styles liked:
• something modern, hip, playful and fun

Colors
0054AA
0677BA
7BADD7
CADEEF
E8F1F8
0094D4
00A9DD
6FCCEA
C7EBF8
E9F6FB
00AB8E
00BBA5
67D7C9
C6EFE9
E9F9F6

Requirements
Must have
• Use of existing logo and a play on "spots" or polka dots with symbpolic wording. Must appeal to young parents and kiddos (including hip teens)
Should not have
• SHOULDNT BE OVER THE TOP KIDS.

```html
<!DOCTYPE html>
<html lang="en">
<head>
<meta charset="utf-8">
<title>Maple Lantern Kids is the spot for....</title>
<link rel="stylesheet" href="https://fonts.googleapis.com/css2?family=Pacifico&family=Amatic+SC:wght@700&family=Oswald:wght@500&family=Lilita+One&family=Chewy&family=Montserrat:wght@700&display=swap">
<style>
  :root {
    --ink: #1b384c;
    --royal: #0054aa;
    --ocean: #0677ba;
    --sky: #7badd7;
    --mist: #c7ebf8;
    --azure: #1e93d4;
    --bright: #00a9e0;
    --aqua: #6fccea;
    --emerald: #00ab8e;
    --seafoam: #6fccc2;
    --sage: #b7dfa6;
    --paper: #f1f2f3;
    --white: #ffffff;
  }
  * { margin: 0; padding: 0; box-sizing: border-box; }
  html, body { width: 1050px; height: 1200px; overflow: hidden; background: var(--paper); }
  .canvas {
    width: 1050px; height: 1200px; position: relative;
    background: radial-gradient(ellipse at 50% 62%, #fbfcfc 0%, #f6f7f8 45%, var(--paper) 80%);
  }
  .canvas svg { display: block; }

  .headline { font-family: "Pacifico", cursive; font-size: 78px; text-anchor: middle; }
  .headline-shadow { fill: var(--ink); stroke: var(--ink); stroke-width: 13px; stroke-linejoin: round; }
  .headline-main { fill: var(--white); stroke: var(--ink); stroke-width: 8px; stroke-linejoin: round; paint-order: stroke fill; }

  .cloud-line { fill: none; stroke: var(--ink); stroke-width: 3px; stroke-linecap: round; }
  .sparkle-royal { fill: var(--royal); }
  .sparkle-bright { fill: var(--bright); }

  .spot-ring { fill: none; stroke: var(--ink); stroke-width: 2.6px; }
  .word { text-anchor: middle; dominant-baseline: central; }
  .word-light { fill: var(--white); }
  .word-dark { fill: var(--ink); }
  .type-thin { font-family: "Amatic SC", "Oswald", sans-serif; font-weight: 700; }
  .type-bold { font-family: "Oswald", sans-serif; font-weight: 500; }
  .type-punch { font-family: "Lilita One", "Chewy", cursive; }
  .type-round { font-family: "Chewy", "Lilita One", cursive; }

  .brand-seal { fill: var(--ink); }
  .brand-name { font-family: "Montserrat", sans-serif; font-weight: 700; fill: var(--white); text-anchor: middle; }
</style>
</head>
<body>
<main class="canvas">
  <svg width="1050" height="1200" viewBox="0 0 1050 1200" aria-labelledby="headline-text">
    <path class="cloud-line" d="M488 206 C488 184 522 176 540 190 C550 166 596 160 612 178 C626 158 656 162 664 174 C680 134 740 128 760 158 C776 142 812 152 816 170 C836 164 852 184 848 208"/>
    <path class="sparkle-royal" d="M647 108 Q651 130 672 134 Q651 138 647 160 Q643 138 622 134 Q643 130 647 108 Z"/>
    <path class="sparkle-bright" d="M462 186 Q464 198 476 200 Q464 202 462 214 Q460 202 448 200 Q460 198 462 186 Z"/>

    <g id="headline-text">
      <text class="headline headline-shadow" x="530" y="278">Maple Lantern Kids is</text>
      <text class="headline headline-shadow" x="530" y="378">the spot for....</text>
      <text class="headline headline-main" x="525" y="271">Maple Lantern Kids is</text>
      <text class="headline headline-main" x="525" y="371">the spot for....</text>
    </g>

    <g class="confetti-spots">
      <circle cx="174" cy="550" r="23" fill="var(--emerald)"/>
      <circle cx="502" cy="504" r="21" fill="var(--mist)"/>
      <circle cx="718" cy="524" r="11" fill="var(--emerald)"/>
      <circle cx="536" cy="630" r="18" fill="var(--azure)"/>
      <circle cx="768" cy="620" r="8" fill="var(--sky)"/>
      <circle cx="900" cy="640" r="14" fill="var(--royal)"/>
      <circle cx="248" cy="636" r="7" fill="var(--mist)"/>
      <circle cx="246" cy="750" r="14" fill="var(--bright)"/>
      <circle cx="378" cy="762" r="8" fill="var(--sky)"/>
      <circle cx="702" cy="764" r="22" fill="var(--seafoam)"/>
      <circle cx="136" cy="798" r="36" fill="var(--seafoam)"/>
      <circle cx="294" cy="934" r="24" fill="var(--sky)"/>
      <circle cx="554" cy="920" r="9" fill="var(--emerald)"/>
      <circle cx="776" cy="886" r="9" fill="var(--aqua)"/>
      <circle cx="906" cy="954" r="14" fill="var(--mist)"/>
      <circle cx="698" cy="1010" r="21" fill="var(--mist)"/>
      <circle cx="466" cy="1026" r="23" fill="var(--seafoam)"/>
      <circle cx="197" cy="1040" r="21" fill="var(--mist)"/>
    </g>

    <g class="brand">
      <circle class="brand-seal" cx="513" cy="768" r="100"/>
      <text class="brand-name" x="513" y="762" font-size="17">Maple Lantern Kids</text>
      <text class="brand-name" x="513" y="788" font-size="13">Cedar Hollow, CA</text>
    </g>

    <g class="word-spot" transform="translate(294 546)">
      <circle r="50" fill="var(--royal)"/><ellipse class="spot-ring" cx="2" cy="2" rx="59" ry="57"/>
      <text class="word word-light type-round" font-size="32">Fun</text>
    </g>
    <g class="word-spot" transform="translate(442 578)">
      <circle r="44" fill="var(--bright)"/><ellipse class="spot-ring" cx="2" cy="2" rx="52" ry="50"/>
      <text class="word word-light type-punch" font-size="21">SMILES</text>
    </g>
    <g class="word-spot" transform="translate(597 546)">
      <circle r="46" fill="var(--seafoam)"/><ellipse class="spot-ring" cx="2" cy="2" rx="54" ry="52"/>
      <text class="word word-dark type-thin" font-size="21" y="-11">Exceptional</text>
      <text class="word word-dark type-thin" font-size="21" y="13">Care</text>
    </g>
    <g class="word-spot" transform="translate(848 550)">
      <circle r="46" fill="var(--seafoam)"/><ellipse class="spot-ring" cx="2" cy="2" rx="54" ry="52"/>
      <text class="word word-light type-punch" font-size="25">CHEER</text>
    </g>
    <g class="word-spot" transform="translate(170 666)">
      <circle r="43" fill="var(--sky)"/><ellipse class="spot-ring" cx="2" cy="2" rx="51" ry="49"/>
      <text class="word word-dark type-thin" font-size="24">EDUCATION</text>
    </g>
    <g class="word-spot" transform="translate(331 684)">
      <circle r="42" fill="var(--seafoam)"/><ellipse class="spot-ring" cx="2" cy="2" rx="50" ry="48"/>
      <text class="word word-light type-thin" font-size="28">COMFORT</text>
    </g>
    <g class="word-spot" transform="translate(677 654)">
      <circle r="43" fill="var(--sage)"/><ellipse class="spot-ring" cx="2" cy="2" rx="51" ry="49"/>
      <text class="word word-dark type-thin" font-size="30">CARING</text>
    </g>
    <g class="word-spot" transform="translate(832 716)">
      <circle r="59" fill="var(--bright)"/><ellipse class="spot-ring" cx="2" cy="2" rx="68" ry="65"/>
      <text class="word word-light type-thin" font-size="38">LAUGHTER</text>
    </g>
    <g class="word-spot" transform="translate(310 832)">
      <circle r="44" fill="var(--emerald)"/><ellipse class="spot-ring" cx="2" cy="2" rx="52" ry="50"/>
      <text class="word word-light type-punch" font-size="29">KIDS</text>
    </g>
    <g class="word-spot" transform="translate(673 868)">
      <circle r="46" fill="var(--azure)"/><ellipse class="spot-ring" cx="2" cy="2" rx="54" ry="52"/>
      <text class="word word-light type-bold" font-size="28">HEALTH</text>
    </g>
    <g class="word-spot" transform="translate(866 866)">
      <circle r="46" fill="var(--sky)"/><ellipse class="spot-ring" cx="2" cy="2" rx="54" ry="52"/>
      <text class="word word-dark type-thin" font-size="30">TEENS</text>
    </g>
    <g class="word-spot" transform="translate(166 926)">
      <circle r="60" fill="var(--azure)"/><ellipse class="spot-ring" cx="2" cy="2" rx="69" ry="66"/>
      <text class="word word-light type-bold" font-size="30">AMAZING</text>
    </g>
    <g class="word-spot" transform="translate(445 930)">
      <circle r="40" fill="var(--ocean)"/><ellipse class="spot-ring" cx="2" cy="2" rx="47" ry="46"/>
      <text class="word word-light type-thin" font-size="25">TODDLERS</text>
    </g>
    <g class="word-spot" transform="translate(320 1026)">
      <circle r="42" fill="var(--sage)"/><ellipse class="spot-ring" cx="2" cy="2" rx="50" ry="48"/>
      <text class="word word-dark type-bold" font-size="23">FRIENDS</text>
    </g>
    <g class="word-spot" transform="translate(581 1024)">
      <circle r="46" fill="var(--sky)"/><ellipse class="spot-ring" cx="2" cy="2" rx="54" ry="52"/>
      <text class="word word-light type-punch" font-size="23">FAMILY</text>
    </g>
    <g class="word-spot" transform="translate(810 1010)">
      <circle r="50" fill="var(--emerald)"/><ellipse class="spot-ring" cx="2" cy="2" rx="59" ry="56"/>
      <text class="word word-light type-thin" font-size="28">POSITIVITY</text>
    </g>
  </svg>
</main>
</body>
</html>
```